Software Company Business Card

We are looking for a new design of our business card. The design will also be used in the rest of our branding and marketing materials as we want to keep it all uniform. We sell POS software to fine/luxury jewelers and also offer other business services as well to help the jeweler manage their business and need something more updated, technical and fresh, preferably more on the masculine side. We do not want any designs with gems in them but if possible would like to incorporate the circle and arrow in the logo into the design, but not a requirement if you can't make it work. I would like to see a variety of the mix. The colors need to remain our blue and orange and the logo can not change. The squiggly lines have been used as our corporate identity for over 20 years and its time to update. Our company name is PELK (Bright Ledger Counter Solutions).

Target Market(s)

High End Jewelers

Industry/Entity Type

Software

Contact Information for Business Card

Requirements
Must have
• Our logo and the colors must remain the same. Blue is #d95d39 and Orange is #0f5682.
Nice to have
• The circle and arrow incorporated but not a requirement.
Should not have
• Anything jewelry or gem related.

```html
<!DOCTYPE html>
<html lang="en">
<head>
<meta charset="utf-8">
<title>PELK Business Card</title>
<link href="https://fonts.googleapis.com/css2?family=Montserrat:wght@400;500;700&display=swap" rel="stylesheet">
<style>
  :root {
    --brand-blue: #05567f;
    --brand-orange: #d95d39;
    --paper: #ffffff;
    --stage: #dadada;
    --title-grey: #5f6366;
    --back-mark: #0a3d5a;
  }
  * { margin: 0; padding: 0; box-sizing: border-box; }
  html, body {
    width: 1200px; height: 1200px; overflow: hidden;
    background: var(--stage);
    font-family: "Montserrat", Arial, sans-serif;
  }
  .card {
    position: absolute;
    left: 219px;
    width: 763px;
    height: 436px;
    overflow: hidden;
  }
  .card-front { top: 115px; background: var(--paper); }
  .card-back { top: 648px; background: var(--brand-blue); }

  .panels { position: absolute; inset: 0; width: 100%; height: 100%; }

  .identity {
    position: absolute;
    right: 47px;
    top: 38px;
    width: 300px;
    text-align: right;
  }
  .person-name {
    font-weight: 500;
    font-size: 33px;
    color: var(--brand-blue);
    line-height: 1.15;
    letter-spacing: 0.3px;
  }
  .person-title {
    font-weight: 400;
    font-size: 19.5px;
    color: var(--title-grey);
    line-height: 1.3;
    letter-spacing: 0.3px;
  }
  .divider {
    height: 1px;
    width: 293px;
    margin-left: auto;
    background: var(--brand-orange);
    margin-top: 14px;
  }
  .brand-mark {
    display: flex;
    justify-content: flex-end;
    align-items: center;
    gap: 14px;
    margin-top: 24px;
  }
  .brand-name {
    font-weight: 700;
    font-size: 64px;
    line-height: 1;
    color: var(--brand-blue);
    letter-spacing: 1px;
  }
  .brand-dot {
    width: 62px; height: 62px;
    border-radius: 50%;
    background: var(--brand-orange);
    flex: none;
  }

  .contact {
    position: absolute;
    left: 41px;
    top: 194px;
    color: var(--paper);
    font-size: 19px;
    font-weight: 400;
    letter-spacing: 0.3px;
  }
  .address { font-style: normal; line-height: 24px; }
  .channels { list-style: none; margin-top: 12px; }
  .channels li {
    display: flex; align-items: center; gap: 9px;
    line-height: 24.5px;
  }
  .channels svg { width: 13px; height: 13px; flex: none; }

  .back-mark {
    position: absolute;
    inset: 0;
    display: flex; align-items: center; justify-content: center;
    gap: 28px;
  }
  .back-mark .brand-name { font-size: 110px; color: var(--back-mark); }
  .back-mark .brand-dot { width: 102px; height: 102px; background: var(--back-mark); }
</style>
</head>
<body>

<section class="card card-front">
  <svg class="panels" viewBox="0 0 763 436" aria-hidden="true">
    <path fill="var(--brand-blue)" d="M0,100 H240 L550,340 H763 V436 H0 Z"/>
    <path fill="var(--brand-orange)" d="M0,72 H240 L550,312 H763 V332 H550 L240,92 H0 Z"/>
    <path fill="var(--brand-blue)" d="M460,214 L560,291 H763 V303 H560 Z"/>
  </svg>

  <div class="identity">
    <h1 class="person-name">Dorian Vessely</h1>
    <p class="person-title">Director of Global Operations</p>
    <div class="divider"></div>
    <div class="brand-mark">
      <span class="brand-name">PELK</span>
      <span class="brand-dot"></span>
    </div>
  </div>

  <div class="contact">
    <address class="address">
      4815 Meridian Parkway<br>
      Suite 210<br>
      Silverbend, NV 89000<br>
      USA
    </address>
    <ul class="channels">
      <li>
        <svg viewBox="0 0 16 16"><path fill="none" stroke="var(--brand-orange)" stroke-width="1.6" d="M4,1.5 L6,5 L4.5,6.5 C5.5,9 7,10.5 9.5,11.5 L11,10 L14.5,12 L13,14.5 C7,14 2,9 1.5,3 Z"/></svg>
        <span>+1 555 214-3307</span>
      </li>
      <li>
        <svg viewBox="0 0 16 16"><rect x="4" y="1" width="8" height="4" fill="var(--brand-orange)"/><rect x="1" y="5" width="14" height="7" rx="1.5" fill="var(--brand-orange)"/><rect x="4" y="10" width="8" height="5" fill="var(--brand-orange)" stroke="var(--brand-blue)" stroke-width="1"/></svg>
        <span>+1 555 386-1942</span>
      </li>
      <li>
        <svg viewBox="0 0 16 16"><rect x="1" y="3" width="14" height="10" fill="none" stroke="var(--brand-orange)" stroke-width="1.5"/><path d="M1,3 L8,9 L15,3" fill="none" stroke="var(--brand-orange)" stroke-width="1.5"/></svg>
        <span>dorian@pelkledger.com</span>
      </li>
      <li>
        <svg viewBox="0 0 16 16"><g fill="none" stroke="var(--brand-orange)" stroke-width="1.2"><circle cx="8" cy="8" r="6.5"/><ellipse cx="8" cy="8" rx="3" ry="6.5"/><path d="M1.5,8 H14.5 M2.5,4.5 H13.5 M2.5,11.5 H13.5"/></g></svg>
        <span>www.pelkledger.com</span>
      </li>
    </ul>
  </div>
</section>

<section class="card card-back">
  <div class="back-mark">
    <span class="brand-name">PELK</span>
    <span class="brand-dot"></span>
  </div>
</section>

</body>
</html>
```